Wordpress Web Design For Midlife Lane.com

We're looking to update the design for www.midlifelane.example. The website provides news and views for people aged 50 plus.

We want to use Wordpress as the content management tool and incorporate postwren to manage subscribers to our monthly newsletter.

In terms of design, we're looking for something simple and straightforward, we quite like the elder hub site, so something like that would be good. http://www.elderhub.example.org
Updates

Project Deadline Extended
Reason: Dear All, Due to the Xmas break in the UK I've decided to extend the deadline by 7 days. Thanks for all your submissions, we will be making a decision shortly. Please note, as per the original brief, we are only interested in fully coded sites uploaded to our hosting provider. Please withdraw your design if you are not able to offer this complete solution. Thanks and good wishes to all!

Requirements
Must have
• Fully working wordpress templates that allow us to easily manage the website content. Easy for readers to use, navigate and read the content.
• Ideally a'turnkey' solution - the website built and ready for us to use wordpress to populate with content.

```html
<!DOCTYPE html>
<html lang="en">
<head>
<meta charset="utf-8">
<title>Midlife Lane.com – News and views for 50 plus</title>
<link href="https://fonts.googleapis.com/css2?family=Open+Sans:wght@400;600&display=swap" rel="stylesheet">
<style>
:root{
  --green:#6fb51f; --green-dark:#5a9f14; --green-light:#8cc63f;
  --orange:#fb8a2b; --purple:#9c3fd2; --pink:#f2579f;
  --text:#444; --muted:#a5a5a5; --border:#dcdcdc; --footer:#2e2e2e;
  --teal:#5fd0c6; --olive:#b5ad7a; --salmon:#f6a0a0; --magenta:#e85aa8; --sage:#9bc2a8; --lilac:#c79ce8; --mustard:#e6c45a;
}
*{box-sizing:border-box;margin:0;padding:0}
html,body{width:879px;height:1200px;overflow:hidden}
body{position:relative;background:linear-gradient(#fff,#f3f3f3 300px,#f3f3f3);font-family:"Open Sans",Arial,sans-serif;color:var(--text)}
.abs{position:absolute}
.brand{left:60px;top:34px;display:flex;align-items:center;gap:8px;font-size:19px;font-weight:600;color:var(--green)}
.brand-dot{width:14px;height:14px;border-radius:50%;background:var(--green)}
.search{left:605px;top:54px;width:217px;height:24px;border:1px solid var(--border);border-radius:12px;background:#fff;font-size:10px;font-style:italic;color:#999;padding:5px 10px}
.search svg{position:absolute;right:8px;top:5px}
.nav{left:58px;top:90px;width:764px;height:37px;display:flex;background:#fff;border:1px solid #e6e6e6}
.nav a{flex:1;text-align:center;font-size:12.5px;color:#444;text-decoration:none;line-height:32px;border-bottom:4px solid;border-right:1px solid #eee}
.nav a.active{background:var(--green);color:#fff;border-bottom-color:var(--green)}
.panel{left:58px;top:127px;width:764px;height:963px;background:#fff}
.ph{display:block}
.hero{left:65px;top:134px;width:523px;height:234px;background:linear-gradient(120deg,#c7a58e,#e7d1bf 45%,#cfc2b8 70%,#a89180)}
.hero-toggle{left:555px;top:340px;width:33px;height:28px;background:var(--green);border-radius:14px 0 0 0}
.section-title{left:72px;top:382px;font-size:16px;color:#555}
.card{position:absolute;width:169px;height:159px;border:1px solid var(--border);background:#fff}
.card .ph{height:77px}
.card h3{font-weight:400;font-size:12px;line-height:16px;color:#555;margin:10px 12px 2px}
.card p{font-size:8px;line-height:13px;color:var(--muted);margin:0 12px}
.card .sub{color:#666;font-size:8.5px}
.promo{left:596px;width:216px;color:#fff;padding:10px 16px}
.promo h2{font-size:17px;font-weight:400}
.promo p{font-size:8px;line-height:11px;opacity:.85}
.register{top:134px;height:88px;background:linear-gradient(var(--orange),#f97a1a)}
.register b{display:block;font-size:8.5px;margin-top:8px}
.newsletter{top:227px;height:98px;background:var(--purple)}
.newsletter .field{margin-top:8px;height:20px;background:#fff;border-radius:3px;position:relative}
.newsletter svg{position:absolute;right:5px;top:3px}
.donate{left:596px;top:330px;width:216px;height:158px;border:1px solid var(--border);background:#fff}
.donate .ph{height:94px;background:linear-gradient(90deg,#6f5a4a,#b9a08a 50%,#a55a46)}
.donate h2{color:var(--pink);font-weight:400;font-size:15px;margin:6px 15px 2px}
.donate p{font-size:8px;line-height:13px;color:var(--muted);margin:0 15px}
.products{left:598px;top:497px;width:214px;height:243px;background:linear-gradient(var(--green-light),var(--green-dark));color:#fff}
.products h2{font-weight:400;font-size:16px;padding:8px 20px;border-bottom:1px solid rgba(255,255,255,.35)}
.products ul{list-style:none;padding:6px 24px}
.products li{font-size:9.5px;height:22.4px;line-height:22px;border-bottom:1px solid rgba(255,255,255,.2);display:flex;align-items:center;gap:6px}
.products li:last-child{border:0}
.blog{left:598px;top:752px;width:214px;height:320px;border:1px solid var(--border);background:#fff}
.blog h2{background:linear-gradient(#f66cad,var(--pink));color:#fff;font-weight:400;font-size:15px;padding:9px 15px;height:38px}
.blog article{margin:12px 15px 0 16px}
.blog h4{font-weight:400;font-size:9.5px;color:#555;margin-bottom:4px}
.blog p{font-size:7.6px;line-height:12px;color:#777}
.footer{left:0;top:1090px;width:879px;height:110px;background:var(--footer);font-family:Arial,sans-serif;color:#eee}
.footer .row{position:absolute;left:75px;font-size:11px;word-spacing:0}
.footer .row span{margin:0 11px;color:#bbb}
.footer small{position:absolute;left:73px;top:68px;font-size:8px;color:#ccc}
</style>
</head>
<body>
<div class="abs brand"><span class="brand-dot"></span>Midlife Lane.com</div>
<div class="abs search">Search here..<svg width="12" height="12" viewBox="0 0 12 12"><circle cx="5" cy="5" r="4" fill="none" stroke="#777" stroke-width="1.4"/><line x1="8" y1="8" x2="11" y2="11" stroke="#777" stroke-width="1.4"/></svg></div>
<nav class="abs nav">
  <a class="active">Home</a><a style="border-bottom-color:var(--teal)">Travel</a><a style="border-bottom-color:var(--olive)">Health</a><a style="border-bottom-color:var(--salmon)">Hobbies</a><a style="border-bottom-color:var(--magenta)">Lifestyle</a><a style="border-bottom-color:var(--sage)">Insurance</a><a style="border-bottom-color:var(--lilac)">Legal</a><a style="border-bottom-color:var(--mustard)">Competitions</a><a style="border-bottom-color:var(--green)">Survey</a>
</nav>
<div class="abs panel"></div>
<div class="abs hero" role="img" aria-label="Group of smiling mature adults"></div>
<div class="abs hero-toggle"><svg width="33" height="28" viewBox="0 0 33 28"><path d="M14 9 l-5 5 5 5 M19 9 l5 5 -5 5" stroke="#fff" stroke-width="2" fill="none"/></svg></div>
<h2 class="abs section-title" style="font-weight:400">Featured Articles</h2>

<div class="card" style="left:70px;top:413px"><div class="ph" role="img" aria-label="Cruise ship at sunset" style="background:linear-gradient(#e9a53a,#a0622a)"></div><h3>Cruise your way to<br>a holiday bargain</h3><p>Cum sociis natoque penatibus et magnis dis parturient montes</p></div>
<div class="card" style="left:245px;top:413px"><div class="ph" role="img" aria-label="Friends out shopping" style="background:linear-gradient(90deg,#b98e6e,#d3b090,#8f6e52)"></div><h3>Are you a last minute<br>Christmas shopper</h3><p>Cum sociis natoque penatibus et magnis dis parturient montes</p></div>
<div class="card" style="left:420px;top:413px"><div class="ph" role="img" aria-label="Woman stretching on grass" style="background:linear-gradient(#5e9bd6,#b7d2e8 55%,#6a9b3c)"></div><h3>You're Never Too Old<br>For Exercise</h3><p>Cum sociis natoque penatibus et magnis dis parturient montes</p></div>

<div class="card" style="left:70px;top:580px"><div class="ph" role="img" aria-label="Cats and dogs together" style="background:linear-gradient(90deg,#f2f2f2,#d8cfc6,#f2f2f2)"></div><h3>Protect Your Pets From<br>Hazards This Christmas</h3><p>Cum sociis natoque penatibus et magnis dis parturient montes</p></div>
<div class="card" style="left:245px;top:580px"><div class="ph" role="img" aria-label="Couple cycling outdoors" style="background:linear-gradient(#6e9bc6,#8ba86a 60%,#5c6f3c)"></div><h3>How Hobbies Help<br>Make You Happy</h3><p>Cum sociis natoque penatibus et magnis dis parturient montes</p></div>
<div class="card" style="left:420px;top:580px"><div class="ph" role="img" aria-label="House energy efficiency rating graphic" style="background:linear-gradient(90deg,#fff,#eef5e6 40%,#f7e1c8 70%,#fff)"></div><h3>Top Ten Tips for keeping</h3><p class="sub">homes warm and energy bills down</p><p>Cum sociis natoque penatibus et magnis dis parturient montes</p></div>

<div class="card" style="left:70px;top:745px"><div class="ph" role="img" aria-label="Therapy massage candle jar" style="background:radial-gradient(circle,#e9e4da 25%,#fff 60%)"></div><h3>Lunara Therapy Massage<br>Candle</h3><p>Cum sociis natoque penatibus et magnis dis parturient montes</p></div>
<div class="card" style="left:245px;top:745px"><div class="ph" role="img" aria-label="Walking boots product with hound" style="background:radial-gradient(circle,#d8c6b0 20%,#fff 60%)"></div><h3>These Boots are made<br>for Walking</h3><p>Cum sociis natoque penatibus et magnis dis parturient montes</p></div>
<div class="card" style="left:420px;top:745px"><div class="ph" style="background:var(--green-dark);color:#fff;text-align:center;font-size:11px;font-weight:600;padding-top:10px;line-height:16px">Win £100 to<br>spend at<br><span style="display:inline-block;background:#111;padding:2px 6px;margin-top:3px;font-weight:400">Hartwell's</span></div><h3>Win £100 to spend at Hartwell's</h3><p>Cum sociis natoque penatibus et magnis dis parturient montes</p></div>

<div class="card" style="left:70px;top:913px"><div class="ph" role="img" aria-label="Smiling older woman" style="background:linear-gradient(90deg,#6d8a5e,#b8c6d0 50%,#e0c8a8)"></div><h3>Life Starts at 60</h3><p>Cum sociis natoque penatibus et magnis dis parturient montes</p></div>
<div class="card" style="left:245px;top:913px"><div class="ph" role="img" aria-label="Passenger train at a station" style="background:linear-gradient(#c9ced6,#6f4b6b 55%,#3d3d3d)"></div><h3>Westcountry Farm Pork Pie</h3><p>Cum sociis natoque penatibus et magnis dis parturient montes</p></div>
<div class="card" style="left:420px;top:913px"><div class="ph" role="img" aria-label="Jar of beauty cream" style="background:radial-gradient(circle,#dde3d8 22%,#fff 55%)"></div><h3>Beauty in Bee Venom</h3><p>Cum sociis natoque penatibus et magnis dis parturient montes</p></div>

<div class="abs promo register"><h2>Register Now</h2><p>Cum sociis natoque penatibus et magnis dis parturient montes, nascetur ridiculus mus</p><b>CLICK HERE TO REGISTER NOW ›</b></div>
<div class="abs promo newsletter"><h2>Sign Up Newsletters</h2><p>Cum sociis natoque penatibus et magnis dis parturient montes, nascetur ridiculus mus</p><div class="field"><svg width="14" height="14" viewBox="0 0 14 14"><circle cx="7" cy="7" r="6" fill="none" stroke="#999" stroke-width="1.3"/><path d="M4 7h6M7.5 4.5 10 7 7.5 9.5" stroke="#999" stroke-width="1.3" fill="none"/></svg></div></div>
<div class="abs donate"><div class="ph" role="img" aria-label="Volunteers at a clothing donation stall"></div><h2>Donate today</h2><p>Cum sociis natoque penatibus et magnis dis parturient montes, nascetur ridiculus mus</p></div>
<div class="abs products"><h2>Latest Products</h2><ul>
<li><svg width="10" height="10"><circle cx="5" cy="5" r="5" fill="#fff"/><path d="M4 2.5 6.5 5 4 7.5" stroke="#6fb51f" stroke-width="1.5" fill="none"/></svg>Etiam est nunc</li>
<li><svg width="10" height="10"><circle cx="5" cy="5" r="5" fill="#fff"/><path d="M4 2.5 6.5 5 4 7.5" stroke="#6fb51f" stroke-width="1.5" fill="none"/></svg>Venenatis in tristique eu</li>
<li><svg width="10" height="10"><circle cx="5" cy="5" r="5" fill="#fff"/><path d="M4 2.5 6.5 5 4 7.5" stroke="#6fb51f" stroke-width="1.5" fill="none"/></svg>Imperdiet ac nisl</li>
<li><svg width="10" height="10"><circle cx="5" cy="5" r="5" fill="#fff"/><path d="M4 2.5 6.5 5 4 7.5" stroke="#6fb51f" stroke-width="1.5" fill="none"/></svg>Cum sociis natoque</li>
<li><svg width="10" height="10"><circle cx="5" cy="5" r="5" fill="#fff"/><path d="M4 2.5 6.5 5 4 7.5" stroke="#6fb51f" stroke-width="1.5" fill="none"/></svg>Penatibus et magnis</li>
<li><svg width="10" height="10"><circle cx="5" cy="5" r="5" fill="#fff"/><path d="M4 2.5 6.5 5 4 7.5" stroke="#6fb51f" stroke-width="1.5" fill="none"/></svg>Dis parturient montes</li>
<li><svg width="10" height="10"><circle cx="5" cy="5" r="5" fill="#fff"/><path d="M4 2.5 6.5 5 4 7.5" stroke="#6fb51f" stroke-width="1.5" fill="none"/></svg>Nascetur ridiculus mus</li>
<li><svg width="10" height="10"><circle cx="5" cy="5" r="5" fill="#fff"/><path d="M4 2.5 6.5 5 4 7.5" stroke="#6fb51f" stroke-width="1.5" fill="none"/></svg>Aculis facilisis massa</li>
</ul></div>
<div class="abs blog"><h2>Recent Blog Post</h2>
<article><h4>Cum sociis natoque penatibus</h4><p>Ut nisi erat, fermentum vel, congue id, euismod in, elit. Fusce ultricies, orci ac feugiat suscipit, leo massa sodales velit, et scelerisque</p></article>
<article><h4>Donec scelerisque leo</h4><p>Ut nisi erat, fermentum vel, congue id, euismod in, elit. Fusce ultricies, orci ac feugiat suscipit</p></article>
<article><h4>Class aptent taciti sociosqu</h4><p>Ut nisi erat, fermentum vel, congue id, euismod in, elit. Fusce ultricies, orci ac feugiat suscipit</p></article>
<article><h4>Bibendum accumsa</h4><p>Ut nisi erat, fermentum vel, congue id, euismod in, elit. Fusce ultricies, orci ac feugiat suscipit, leo massa sodales velit, et scelerisque mi Phasellus felis dolor, scelerisque a, tempus eget, lobortis id, libero. Donec scelerisq</p></article>
</div>
<footer class="abs footer">
  <div class="row" style="top:24px">Home<span>|</span>Travel<span>|</span>Health<span>|</span>Hobbies<span>|</span>Lifestyle<span>|</span>Insurance<span>|</span>Legal<span>|</span>Competitions<span>|</span>Survey</div>
  <div class="row" style="top:46px;left:74px">About Us<span>|</span>Advertise<span>|</span>Support<span>|</span>Blog<span>|</span>Contact</div>
  <small>Copyright © 2013 Midlife Lane. All Rights Reserved.</small>
</footer>
</body>
</html>
```